Chartered Professional Accounting Firm Needs a Business Card Design

We need a card design for an accounting firm based in Toronto, Ontario. The firm name is Leo Dart Professional Corporation. The owner of the firm is a chartered professional accountant and a certified general accountant. Services of the firm include 60% tax preparation and consulting and 40% financial statements for corporation year-end. We would like a modern design. The color could be black, white, gray, blue or other color to bring more confidence to clients. The logo of the firm should be included in the design. Thanks

Name: Leo Dart, CPA, CGA Address: 47 Amberfield Cres. Richmond Hill, ON M3K 7P2 Telephone: (416) 555-0137 Fax:(416) 555-0192 Email: leo@leodart.example

Accounting

```html
<!DOCTYPE html>
<html lang="en">
<head>
<meta charset="utf-8">
<title>Leo Dart Professional Corporation – Business Card</title>
<link rel="stylesheet" href="https://fonts.googleapis.com/css2?family=Cinzel:wght@400;700&display=swap">
<style>
  :root {
    --backdrop: #1c1c1e;
    --navy-deep: #141a5c;
    --navy: #232d8c;
    --navy-light: #3442b0;
    --paper: #f4f4f6;
    --silver: #a9abb2;
    --silver-light: #d4d5da;
    --rule-blue: #4a8fe0;
    --ink-white: #ffffff;
    --brand-ink: #1f2a86;
  }
  * { margin: 0; padding: 0; box-sizing: border-box; }
  html, body {
    width: 1200px; height: 900px; overflow: hidden;
    background: var(--backdrop);
  }
  .card {
    position: absolute;
    left: 100px; top: 164px;
    width: 1000px; height: 572px;
    overflow: hidden;
    font-family: "Cinzel", Georgia, serif;
    color: var(--ink-white);
  }
  .card-art { position: absolute; inset: 0; width: 100%; height: 100%; }
  .brand {
    position: absolute; left: 48px; top: 104px;
    display: flex; align-items: center; gap: 14px;
    color: var(--brand-ink); font-weight: 700;
  }
  .brand-mark { width: 56px; height: 56px; background: var(--brand-ink); flex: none; }
  .brand-name { line-height: 1.1; }
  .brand-title { display: block; font-size: 30px; letter-spacing: 0.5px; }
  .brand-sub { display: block; font-size: 12.5px; letter-spacing: 0.6px; }
  .brand-tagline {
    display: block; font-size: 8.5px; font-weight: 400;
    letter-spacing: 0.5px; line-height: 1.25;
  }
  .brand-tagline:first-of-type { margin-top: 3px; }
  .holder {
    position: absolute; left: 440px; top: 212px; width: 490px;
  }
  .holder-name {
    font-size: 38px; font-weight: 400; letter-spacing: 1px;
    padding-bottom: 8px;
    border-bottom: 1px solid var(--rule-blue);
  }
  .holder-name small { font-size: 26px; }
  .contact {
    margin-top: 14px; text-align: right; list-style: none;
    font-size: 19px; line-height: 1.6; letter-spacing: 0.5px;
  }
  .address {
    position: absolute; left: 250px; top: 482px;
    font-size: 17px; letter-spacing: 0.8px;
  }
</style>
</head>
<body>
  <article class="card">
    <svg class="card-art" viewBox="0 0 1000 572" preserveAspectRatio="none" aria-hidden="true">
      <defs>
        <radialGradient id="field-blue" cx="0.45" cy="0.55" r="0.75">
          <stop offset="0" stop-color="var(--navy-light)"/>
          <stop offset="0.55" stop-color="var(--navy)"/>
          <stop offset="1" stop-color="var(--navy-deep)"/>
        </radialGradient>
        <linearGradient id="band-silver" x1="0" y1="1" x2="1" y2="0">
          <stop offset="0" stop-color="var(--silver)"/>
          <stop offset="1" stop-color="var(--silver-light)"/>
        </linearGradient>
      </defs>
      <rect class="field" width="1000" height="572" fill="url(#field-blue)"/>
      <path class="wave-band" fill="url(#band-silver)"
        d="M0 0 H760 C600 50 500 170 360 250 C240 318 100 330 0 470 Z"/>
      <path class="wave-paper" fill="var(--paper)"
        d="M0 0 H720 C565 45 470 155 335 232 C220 298 90 310 0 440 Z"/>
    </svg>

    <div class="brand">
      <div class="brand-mark"></div>
      <div class="brand-name">
        <span class="brand-title">Leo Dart</span>
        <span class="brand-sub">Professional Corporation</span>
        <span class="brand-tagline">Chartered Professional Accountants</span>
        <span class="brand-tagline">Certified General Accountants</span>
      </div>
    </div>

    <div class="holder">
      <h1 class="holder-name">Leo Dart, <small>CPA, CGA</small></h1>
      <ul class="contact">
        <li>Telephone (416) 555-0137</li>
        <li>Fax (416) 555-0192</li>
        <li>Email: leo@leodart.example</li>
      </ul>
    </div>

    <p class="address">47 Amberfield Cres. Richmond Hill, ON M3K 7P2</p>
  </article>
</body>
</html>
```